Design an e-commerce website for a suntan product
Look at these websites before submitting a new idea.
Palm Springs is in desert.
Famous movie stars and wealthy people have homes here and the annual film festival draws people from all over the world.
This should take on a 70's retro look.
https://seecoralmesa.com/
sleeklinedays.com

Target Market(s)

Sunbathers who want a dark tan. product does not contain any sunscreen.

Industry/Entity Type

Cosmetic

Coding

Coded - Design and coding required

Number of Pages Required

2 page

Requirements
Must have
• IMPORTANT
Retro look. go to: https://seecoralmesa.com/
and https://www.sleeklinedays.com/ to have an idea about retro.
Nice to have
• Look at these websites before submitting a new idea.
sleeklinedays.com
Should not have
• Any sexual content

```html
<!DOCTYPE html>
<html lang="en">
<head>
<meta charset="utf-8">
<title>Sunvale Glowtan — Suntan Product</title>
<link rel="stylesheet" href="https://fonts.googleapis.com/css2?family=Poppins:wght@400;500;600;700;800&family=Righteous&display=swap">
<style>
:root{
  --red:#d3322f;
  --orange:#e9761f;
  --mustard:#f0b23a;
  --brown:#7a2e12;
  --maroon:#4a0a0c;
  --ink:#2b1412;
  --text:#3b2f2d;
  --beige:#f3e7de;
  --blush:#efe2e0;
  --footer:#5a0712;
  --footer-line:#7a2630;
  --white:#ffffff;
  --grey:#e4e4e4;
  --star:#f2a21b;
}
*{box-sizing:border-box;margin:0;padding:0}
html,body{width:1200px;height:3941px;overflow:hidden;background:var(--white)}
body{position:relative;font-family:'Poppins',sans-serif;color:var(--text)}
a{color:inherit;text-decoration:none}

/* retro stripe band: red / orange / mustard */
.stripes{position:absolute;display:flex;flex-direction:column}
.stripes span{display:block;flex:1}
.stripes span:nth-child(1){background:var(--red)}
.stripes span:nth-child(2){background:var(--orange)}
.stripes span:nth-child(3){background:var(--mustard)}
.stripes.row{flex-direction:row}

/* header */
.site-header{position:absolute;left:0;top:0;width:1200px;height:66px;background:var(--white);z-index:5}
.brand{position:absolute;left:89px;top:10px;font-weight:700;font-size:22px;line-height:22px;color:var(--maroon);width:150px}
.main-nav{position:absolute;left:476px;top:23px;display:flex;gap:28px;font-size:15px;font-weight:500;color:var(--maroon)}
.nav-icons{position:absolute;left:1026px;top:23px;display:flex;gap:12px}
.cart-count{position:absolute;left:1098px;top:20px;width:13px;height:13px;border-radius:50%;background:var(--red);color:#fff;font-size:8px;text-align:center;line-height:13px}

/* hero */
.hero{position:absolute;left:0;top:66px;width:1200px;height:676px;overflow:hidden;background:linear-gradient(110deg,#e8ddd0 0%,#f2e9e0 45%,#ece1d6 100%)}
.hero-leaf{position:absolute;border-radius:50%;background:linear-gradient(140deg,#7d9a74,#3e5c3f)}
.retro-sun{position:absolute;left:560px;top:96px}
.hero-bottle{position:absolute;left:655px;top:190px;width:220px;height:380px;border-radius:46px 46px 36px 36px;background:linear-gradient(150deg,#e87a1c,#b8450f 55%,#6a1a08);transform:rotate(35deg)}
.hero-kicker{position:absolute;left:84px;top:296px;font-family:'Righteous',sans-serif;font-size:54px;color:var(--red);line-height:1}
.hero-title{position:absolute;left:84px;top:342px;font-size:96px;font-weight:800;color:var(--maroon);line-height:1;letter-spacing:-1px}
.hero-text{position:absolute;left:89px;top:440px;width:440px;font-size:16.5px;line-height:23px;color:var(--ink)}
.btn{display:inline-block;background:var(--red);color:#fff;font-weight:700;text-align:center}
.hero-btn{position:absolute;left:89px;top:493px;width:136px;height:38px;line-height:38px;font-size:17px;border-radius:19px}

/* featured */
.photo{position:absolute}
.kicker{font-family:'Righteous',sans-serif;font-size:26px;color:var(--red)}
.section-heading{font-size:44px;font-weight:800;color:var(--maroon);line-height:1}
.featured-copy{position:absolute;left:729px;top:968px;width:385px}
.featured-copy .section-heading{margin-top:4px}
.featured-copy p{margin-top:16px;font-size:14px;line-height:21px}
.btn-outline{display:inline-block;margin-top:12px;width:147px;height:38px;line-height:34px;border:2px solid var(--red);border-radius:19px;font-weight:700;font-size:16px;text-align:center;color:var(--maroon)}

/* promo */
.promo-panel{position:absolute;left:89px;top:1443px;width:509px;height:372px;background:var(--beige);overflow:hidden}
.promo-circle{position:absolute;left:808px;top:1665px;width:190px;height:190px;border-radius:50%;background:var(--blush)}
.promo-copy{position:absolute;left:152px;top:1541px;width:300px}
.promo-copy .section-heading{font-size:36px}
.promo-copy p{margin-top:12px;font-size:14px;line-height:21px}
.promo-copy .btn{margin-top:14px;width:126px;height:35px;line-height:35px;font-size:16px;border-radius:18px}
.promo-list{position:absolute;left:150px;top:1858px;width:300px;font-size:14px;line-height:21px}
.promo-list ul{list-style:none;margin-top:6px}
.promo-list li{display:flex;align-items:center;gap:6px}
.promo-bottle{position:absolute;left:471px;top:1507px;width:249px;height:538px;border-radius:110px 110px 50px 50px;background:linear-gradient(90deg,#5e1106,#a53a0c 35%,#d86a14 55%,#8c2a08 85%,#4e0d05)}
.palm-leaf{position:absolute;left:930px;top:1944px;width:270px;height:400px;border-radius:60% 0 0 40%;background:linear-gradient(200deg,#4f7a3f,#9cbb86);opacity:.9}

/* tips */
.center-title{position:absolute;left:0;width:1200px;text-align:center}
.title-rule{position:absolute;left:560px;width:80px;height:12px}
.blog-card{position:absolute;top:2204px;width:332px;height:395px;background:#fff;box-shadow:0 6px 18px rgba(0,0,0,.06);z-index:2}
.blog-card .thumb{height:214px}
.blog-card .body{padding:26px 30px 0 37px}
.blog-card h3{font-size:21px;font-weight:700;color:var(--maroon)}
.blog-card p{margin-top:4px;font-size:13.5px;line-height:20.5px}
.blog-card .more{display:block;margin-top:6px;font-size:13px;font-weight:600;color:var(--red)}

/* reviews */
.review{position:absolute;top:2763px;width:419px;height:245px;border-radius:60px;background:#fff;box-shadow:0 8px 24px rgba(0,0,0,.07)}
.review .avatar{position:absolute;left:47px;top:34px;width:70px;height:70px;border-radius:50%;background:linear-gradient(#d6c2b8,#8f7a70)}
.review .who{position:absolute;left:134px;top:52px;font-size:13px;line-height:18px}
.review .who b{display:block;font-weight:700;color:var(--ink)}
.review .quote{position:absolute;right:40px;top:34px}
.review p{position:absolute;left:47px;top:118px;width:340px;font-size:14px;line-height:21.5px}
.review .stars{position:absolute;left:47px;top:186px;color:var(--star);font-size:15px;letter-spacing:3px}
.dots{position:absolute;top:3032px;left:573px;display:flex;gap:6px}
.dots span{width:12px;height:12px;border-radius:50%;background:var(--grey)}
.dots span.on{background:var(--red)}

/* instagram */
.insta{position:absolute;left:0;top:3171px;width:1200px;height:216px;display:flex}
.insta div{flex:1}

/* newsletter */
.newsletter-title{position:absolute;left:87px;top:3428px;font-size:44px;font-weight:800;color:var(--maroon);line-height:1}
.newsletter-sub{position:absolute;left:87px;top:3478px;font-size:18px;color:var(--ink)}
.news-input{position:absolute;left:539px;top:3449px;width:407px;height:52px;background:#fff;box-shadow:0 2px 10px rgba(0,0,0,.08);padding-left:26px;line-height:52px;font-size:20px;color:#b4b4b4}
.news-btn{position:absolute;left:946px;top:3449px;width:165px;height:52px;line-height:52px;font-size:18px}

/* footer */
.site-footer{position:absolute;left:0;top:3543px;width:1200px;height:398px;background:var(--footer);color:#fff}
.footer-brand{position:absolute;left:119px;top:150px;font-size:32px;font-weight:700;line-height:34px}
.footer-col{position:absolute;top:122px}
.footer-col h4{font-size:20px;font-weight:700;margin-bottom:10px}
.footer-col li{list-style:none;font-size:14px;line-height:24.3px}
.socials{position:absolute;left:911px;top:175px;display:flex;gap:8px}
.socials span{width:34px;height:34px;border-radius:50%;background:var(--footer-line)}
.to-top{position:absolute;left:1134px;top:328px;width:40px;height:40px;border-radius:50%;background:var(--red)}
.footer-rule{position:absolute;left:89px;top:352px;width:1022px;height:1px;background:var(--footer-line)}
.copyright{position:absolute;left:89px;top:368px;font-size:13px;font-weight:600}
.pay{position:absolute;top:362px;display:flex;gap:10px;left:969px}
.pay span{width:40px;height:28px;border-radius:4px;background:#fff}
.pay span.dark{background:#3a4fb4}
</style>
</head>
<body>

<header class="site-header">
  <div class="brand">sunvale<br>glowtan</div>
  <nav class="main-nav"><a>Shop</a><a>Products</a><a>About Us</a><a>Sun Safety</a><a>FAQ</a><a>Contact Us</a></nav>
  <div class="nav-icons">
    <svg width="18" height="18" viewBox="0 0 18 18" aria-label="Search"><circle cx="7.5" cy="7.5" r="5.5" fill="none" stroke="#2b1412" stroke-width="2"/><line x1="11.5" y1="11.5" x2="16" y2="16" stroke="#2b1412" stroke-width="2"/></svg>
    <svg width="18" height="18" viewBox="0 0 24 24" aria-label="Wishlist"><path d="M12 21s-9-6-9-12a5 5 0 0 1 9-3 5 5 0 0 1 9 3c0 6-9 12-9 12z" fill="#4a0a0c"/></svg>
    <svg width="20" height="18" viewBox="0 0 24 22" aria-label="Cart"><path d="M1 2h4l3 12h12l3-9H7" fill="none" stroke="#2b1412" stroke-width="2.4"/><circle cx="9" cy="19" r="2" fill="#2b1412"/><circle cx="19" cy="19" r="2" fill="#2b1412"/></svg>
  </div>
  <span class="cart-count">0</span>
</header>

<section class="hero" role="img" aria-label="Sandy beige backdrop with green leaves and gold flecks">
  <svg class="retro-sun" width="440" height="440" viewBox="0 0 440 440">
    <circle cx="220" cy="220" r="210" fill="#f0b23a" opacity=".55"/>
    <circle cx="220" cy="220" r="170" fill="#e9761f" opacity=".45"/>
    <circle cx="220" cy="220" r="130" fill="#d3322f" opacity=".35"/>
  </svg>
  <div class="hero-leaf" style="left:-60px;top:430px;width:170px;height:260px;transform:rotate(-25deg)"></div>
  <div class="hero-leaf" style="left:1020px;top:-60px;width:220px;height:170px;transform:rotate(20deg)"></div>
</section>
<div class="stripes" style="left:0;top:742px;width:1200px;height:18px"><span></span><span></span><span></span></div>
<div class="hero-bottle" role="img" aria-label="Amber bottle of Sunvale Glowtan tanning oil"></div>
<div class="hero-kicker">Suntan</div>
<div class="hero-title">Product</div>
<p class="hero-text">#1 dermatologist recommended sun care brand for beach days and every day.</p>
<a class="btn hero-btn">BUY NOW</a>

<section>
  <div class="photo" style="left:89px;top:836px;width:477px;height:419px;background:linear-gradient(160deg,#dfe6e6,#d8c8b6 55%,#d79ec0)" role="img" aria-label="Woman in a sun hat sitting on the beach"></div>
  <div class="photo" style="left:191px;top:1255px;width:303px;height:98px;background:linear-gradient(120deg,#a9d3df,#2f4a2e)" role="img" aria-label="Palm frond shadow on pale blue"></div>
  <div class="photo" style="left:366px;top:1055px;width:295px;height:261px;background:linear-gradient(90deg,#f1e5dc 30%,#c25a1a 50%,#f1e5dc 65%,#4e7a3a)" role="img" aria-label="Tanning oil bottle beside a palm leaf"></div>
  <div class="featured-copy">
    <div class="kicker">Get Glowing!</div>
    <h2 class="section-heading">Featured Fan<br>Favorites</h2>
    <p>Lorem Ipsum is simply dummy text of the printing and typesetting industry. Lorem Ipsum has been the industry's standard dummy text ever since the 1500s, when an unknown printer took a galley.</p>
    <a class="btn-outline">READ MORE</a>
  </div>
</section>

<section>
  <div class="promo-panel">
    <div class="stripes row" style="position:absolute;left:0;top:0;width:36px;height:372px"><span></span><span></span><span></span></div>
  </div>
  <div class="photo" style="left:598px;top:1443px;width:512px;height:254px;background:linear-gradient(135deg,#3f6fc0,#3566b7 60%,#e6b98f)" role="img" aria-label="Starfish and seashells on blue"></div>
  <div class="promo-circle"></div>
  <div class="promo-copy">
    <h2 class="section-heading">Sunvale<br>Glowtan</h2>
    <p>Lorem Ipsum is simply dummy text of the printing and typesetting industry. Lorem Ipsum has been the industry's.</p>
    <a class="btn">BUY NOW</a>
  </div>
  <div class="promo-list">
    <p>Typesetting industry lorem Ipsum has been the industry's.</p>
    <ul>
      <li><svg width="11" height="11" viewBox="0 0 12 12"><circle cx="6" cy="6" r="6" fill="#5aa24a"/><path d="M3 6l2 2 4-4" stroke="#fff" stroke-width="1.6" fill="none"/></svg>It is a long established fact.</li>
      <li><svg width="11" height="11" viewBox="0 0 12 12"><circle cx="6" cy="6" r="6" fill="#5aa24a"/><path d="M3 6l2 2 4-4" stroke="#fff" stroke-width="1.6" fill="none"/></svg>That a reader will be distracted</li>
      <li><svg width="11" height="11" viewBox="0 0 12 12"><circle cx="6" cy="6" r="6" fill="#5aa24a"/><path d="M3 6l2 2 4-4" stroke="#fff" stroke-width="1.6" fill="none"/></svg>By the readable content.</li>
    </ul>
  </div>
  <div class="promo-bottle" role="img" aria-label="Amber tanning oil bottle with white cap"></div>
  <div class="palm-leaf" role="img" aria-label="Green palm frond"></div>
</section>

<h2 class="section-heading center-title" style="top:2140px">Tips &amp; Tools</h2>
<article class="blog-card" style="left:89px">
  <div class="thumb" role="img" aria-label="Sun loungers by an infinity pool with palms" style="background:linear-gradient(180deg,#cfe6f3,#6fb3d6 60%,#e9eef0)"></div>
  <div class="body"><h3>Blog heading here</h3><p>Lorem Ipsum is simply dummy text of the printing and typesetting industry. Lorem Ipsum has been.</p><a class="more">READ MORE</a></div>
</article>
<article class="blog-card" style="left:435px">
  <div class="thumb" role="img" aria-label="Poolside loungers and umbrellas" style="background:linear-gradient(180deg,#d9d5cf,#c7c2ba 50%,#37b6e0)"></div>
  <div class="body"><h3>Blog heading here</h3><p>Lorem Ipsum is simply dummy text of the printing and typesetting industry. Lorem Ipsum has been.</p><a class="more">READ MORE</a></div>
</article>
<article class="blog-card" style="left:779px">
  <div class="thumb" role="img" aria-label="Woman in a straw hat under desert palms" style="background:linear-gradient(180deg,#d8c7ad,#e8b23a 75%,#c9a981)"></div>
  <div class="body"><h3>Blog heading here</h3><p>Lorem Ipsum is simply dummy text of the printing and typesetting industry. Lorem Ipsum has been.</p><a class="more">READ MORE</a></div>
</article>

<h2 class="section-heading center-title" style="top:2691px">Customer Review</h2>
<div class="review" style="left:89px">
  <div class="avatar" role="img" aria-label="Customer portrait"></div>
  <div class="who"><b>MARLA</b>Menlo Park, CA</div>
  <svg class="quote" width="60" height="40" viewBox="0 0 60 40"><path d="M2 38V22C2 10 8 4 20 2v7c-6 2-8 6-8 12h8v17zM32 38V22c0-12 6-18 18-20v7c-6 2-8 6-8 12h8v17z" fill="#ececec"/></svg>
  <p>"Lorem Ipsum has been the industry's standard dummy text ever since the 1500s, when an unknown printer."</p>
  <div class="stars">★★★★★</div>
</div>
<div class="review" style="left:533px">
  <div class="avatar" role="img" aria-label="Customer portrait"></div>
  <div class="who"><b>TOMAS</b>San Carlos, CA</div>
  <svg class="quote" width="60" height="40" viewBox="0 0 60 40"><path d="M2 38V22C2 10 8 4 20 2v7c-6 2-8 6-8 12h8v17zM32 38V22c0-12 6-18 18-20v7c-6 2-8 6-8 12h8v17z" fill="#ececec"/></svg>
  <p>"Lorem Ipsum has been the industry's standard dummy text ever since the 1500s, when an unknown printer."</p>
  <div class="stars">★★★★★</div>
</div>
<div class="review" style="left:980px">
  <div class="avatar" role="img" aria-label="Customer portrait"></div>
  <div class="who"><b>RENATA</b>Palo Alto, CA</div>
  <p>"Lorem Ipsum has been the industry's standard dummy text ever since the 1500s, when an unknown printer."</p>
  <div class="stars">★★★★★</div>
</div>
<div class="dots"><span class="on"></span><span></span><span></span></div>

<h2 class="section-heading center-title" style="top:3105px">#Instagram</h2>
<div class="insta">
  <div role="img" aria-label="Beach umbrella and wooden loungers" style="background:linear-gradient(180deg,#4aa6e0,#e9c58a)"></div>
  <div role="img" aria-label="Sunbather in a striped hat" style="background:linear-gradient(180deg,#c8ccce,#6d6b6a)"></div>
  <div role="img" aria-label="Palm trees against blue sky" style="background:linear-gradient(180deg,#1f7fd0,#5fa63c)"></div>
  <div role="img" aria-label="Tanning oil bottle on a pedestal" style="background:linear-gradient(90deg,#e7ddd2,#b4461a 50%,#e7ddd2)"></div>
  <div role="img" aria-label="Woman in sunglasses in a pool" style="background:linear-gradient(180deg,#9ec3c8,#e0b8a0)"></div>
  <div role="img" aria-label="Tanning oil bottle on white shells" style="background:linear-gradient(135deg,#f3eee6,#d9661a 60%,#f0e9de)"></div>
</div>

<h2 class="newsletter-title">Newsletter</h2>
<p class="newsletter-sub">Subscribe to our newsletter</p>
<div class="news-input">Email Address</div>
<a class="btn news-btn">SUBSCRIBE</a>

<div class="stripes" style="left:0;top:3525px;width:1200px;height:18px"><span></span><span></span><span></span></div>
<footer class="site-footer">
  <div class="footer-brand">sunvale<br>glowtan</div>
  <div class="footer-col" style="left:422px"><h4>Useful Links</h4><ul><li>Shop</li><li>Products</li><li>About Us</li><li>Sun Safety</li><li>FAQ</li><li>Contact Us</li></ul></div>
  <div class="footer-col" style="left:672px"><h4>Online Purchases</h4><ul><li>Order Status</li><li>Ordering &amp; Payments</li><li>Returns &amp; Exchanges</li><li>Shipping Information</li><li>Offers</li></ul></div>
  <div class="socials"><span></span><span></span><span></span><span></span></div>
  <div class="to-top"><svg width="40" height="40" viewBox="0 0 40 40"><path d="M16 22l4-4 4 4" stroke="#fff" stroke-width="2" fill="none"/></svg></div>
  <div class="footer-rule"></div>
  <div class="copyright">©Copyright 2021 | All Rights Reserved</div>
  <div class="pay"><span></span><span class="dark"></span><span></span></div>
</footer>

</body>
</html>
```